Design a poster for Tamsin's Dash 2023. A charity event supporting paediatric brain cancer.

We need a new poster for our event in 2023. The successful applicant will have opportunity for ongoing work with our foundation as we need a number of other deliverables once the design is finalised. We have a strong, fun and youthful brand.
Please see attached PDF showing the last 10 years of designs.
Please see attached moodboards outlining concepts for our 2023 theme. The last image of skateboarder concept is "Velvet Tide" - A retro miami vibe Juxtaposed with photo of someone from one of our previous events. Potentially posters could have multiple variants building on lots of different photos.
I have attached our brand guidelines as well as lock ups for our Tamsin's Dash logos.
Whatever is created needs to be transferrable on to a number of different mediums, most importantly T-shirts, Web Banners, Billboards, Pavement Stickers, Social posts.
Our sponsor logos will remain the same.
Please only send complete designs - aligned with one of the 4 concepts provided and include all copy as per attached and include sponsors logos. Please ensure the body fonts are Brandon Grotesque and CCMatinee Idol.
Updates
Hi All, Thank you so much for all the submissions. Unfortunately after our CEO and team have reviewed the designs they are looking to go in quite a different direction than the original brief provided. I apologise for wasting your time. I have updated brief, and more specific moodboards, the last image concept is "Velvet Tide" - A retro miami vibe Juxtaposed with photo of someone from one of our previous events. Potentially posters could have multiple variants building on lots of different photos . If you would like to submit another design that would be great but if not we completely understand. Thank you again for your creative submissions.
Target Market(s)
18-35 year olds
Industry/Entity Type
Not for Profit - Fun Run Event and Party
Font styles to use
Other font styles liked:
- Fonts in Brand Guidelines - Brandon Grotesque and CCMatinee Idol
Requirements
Must have
- On Brand - colourful, focus on MORE JOY THAN DASH

```html
<!DOCTYPE html>
<html lang="en">
<head>
<meta charset="utf-8">
<title>Tamsin's Dash 2023 Poster</title>
<link rel="stylesheet" href="https://fonts.googleapis.com/css2?family=Jost:wght@500;600;700&family=Graduate&family=Oswald:wght@700&family=Lobster+Two:ital,wght@1,700&display=swap">
<style>
  :root {
    --sand: #f2dfb8;
    --sand-light: #f7e9cc;
    --navy: #13213f;
    --teal: #4fb8b8;
    --sun: #fcc94c;
    --leaf-yellow: #fbc54a;
    --leaf-green: #a9d2c0;
    --coral: #f2977c;
    --paper: #faf6ee;
  }
  * { margin: 0; padding: 0; box-sizing: border-box; }
  html, body { width: 969px; height: 1200px; overflow: hidden; background: var(--sand); }
  .poster {
    position: relative;
    width: 969px; height: 1200px;
    overflow: hidden;
    background: radial-gradient(circle at 50% 260px, var(--sand-light) 0%, var(--sand) 70%);
    font-family: "Jost", sans-serif;
    color: var(--navy);
    text-align: center;
  }
  .deco { position: absolute; }
  .deco--blob-top-left { left: -40px; top: -40px; width: 300px; height: 220px; background: var(--sun); border-radius: 0 0 60% 40%; }
  .deco--palm-top-right { right: 0; top: 0; width: 170px; height: 300px; background: linear-gradient(160deg, var(--leaf-yellow), var(--sand) 85%); border-bottom-left-radius: 100%; }
  .deco--leaves-left { left: 0; top: 560px; width: 150px; height: 320px; background: linear-gradient(90deg, var(--leaf-yellow), var(--sand)); border-top-right-radius: 100%; }
  .deco--monstera { left: 0; top: 860px; width: 220px; height: 260px; background: linear-gradient(135deg, var(--leaf-green), var(--sand) 90%); border-top-right-radius: 70%; }
  .deco--leaves-right { right: 0; top: 740px; width: 130px; height: 220px; background: linear-gradient(270deg, var(--coral), var(--sand) 90%); border-top-left-radius: 100%; }

  .presenter { position: absolute; top: 44px; left: 0; right: 0; font-weight: 600; font-size: 23px; letter-spacing: 0.3px; }

  .sun { position: absolute; left: 422px; top: 186px; width: 126px; height: 126px; border-radius: 50%; background: var(--sun); }

  .event-name { position: absolute; left: 0; right: 0; font-family: "Graduate", sans-serif; color: var(--navy); font-weight: 400; }
  .event-name--first { top: 160px; font-size: 104px; letter-spacing: 18px; padding-left: 18px; }
  .event-name-row { position: absolute; top: 292px; left: 0; right: 0; display: flex; justify-content: center; align-items: center; gap: 46px; }
  .event-name-row .side { font-family: "Jost", sans-serif; font-weight: 600; font-size: 38px; letter-spacing: 1px; }
  .event-name-row .main { font-family: "Graduate", sans-serif; font-size: 100px; letter-spacing: 8px; line-height: 1; }

  .cause { position: absolute; top: 430px; left: 0; right: 0; font-weight: 600; font-size: 27px; line-height: 36px; }

  .wave { position: absolute; left: 355px; width: 260px; height: 14px; }
  .wave--top { top: 524px; }
  .wave--bottom { top: 806px; }

  .headline { position: absolute; left: 0; right: 0; font-weight: 600; font-size: 55px; line-height: 1; letter-spacing: 1px; }
  .headline .script { font-family: "Lobster Two", cursive; font-style: italic; font-weight: 700; font-size: 46px; letter-spacing: 0; }
  .headline--fun { top: 556px; }
  .headline--way { top: 686px; }
  .date { position: absolute; left: 0; right: 0; font-weight: 600; font-size: 46px; color: var(--teal); letter-spacing: 1px; line-height: 1; }
  .date--sunday { top: 620px; }
  .date--month { top: 748px; }

  .register { position: absolute; top: 860px; left: 0; right: 0; font-weight: 600; font-size: 18px; letter-spacing: 2px; }
  .website { position: absolute; top: 894px; left: 0; right: 0; font-family: "Oswald", sans-serif; font-weight: 700; font-size: 52px; letter-spacing: 0.5px; }

  .footer-band { position: absolute; left: 0; bottom: 0; width: 969px; height: 170px; }

  .foundation-mark {
    position: absolute; right: 46px; top: 994px;
    display: flex; align-items: center; gap: 10px;
    font-weight: 600; font-size: 22px; color: var(--navy);
  }
  .foundation-mark .dot { width: 16px; height: 16px; border-radius: 50%; background: var(--navy); }

  .supported { position: absolute; top: 1080px; left: 120px; font-weight: 600; font-size: 15px; letter-spacing: 0.5px; }
  .sponsors { position: absolute; top: 1132px; left: 120px; right: 200px; display: flex; justify-content: space-between; align-items: center; }
  .sponsor { font-family: "Jost", sans-serif; font-weight: 600; font-size: 22px; color: var(--navy); }
</style>
</head>
<body>
<main class="poster">
  <div class="deco deco--blob-top-left" role="img" aria-label="Warm yellow abstract blob"></div>
  <div class="deco deco--palm-top-right" role="img" aria-label="Illustrated yellow palm fronds"></div>
  <div class="deco deco--leaves-left" role="img" aria-label="Illustrated yellow tropical leaves"></div>
  <div class="deco deco--monstera" role="img" aria-label="Illustrated green monstera leaf"></div>
  <div class="deco deco--leaves-right" role="img" aria-label="Illustrated coral tropical leaves"></div>

  <p class="presenter">THE ELLIS TAMSIN HART FOUNDATION PRESENTS</p>

  <div class="sun" role="img" aria-label="Sun with clouds"></div>
  <h1 class="event-name event-name--first">TAMSIN'S</h1>
  <div class="event-name-row">
    <span class="side">SEPT</span>
    <span class="main">DASH</span>
    <span class="side">2023</span>
  </div>

  <p class="cause">HELP US BEAT PADIATRIC BRAIN CANCER<br>THE # 1 DISEASE KILLER OF YOUNG PEOPLE</p>

  <svg class="wave wave--top" viewBox="0 0 240 14" preserveAspectRatio="none" aria-hidden="true">
    <path d="M0 7 q7.5 -6 15 0 t15 0 t15 0 t15 0 t15 0 t15 0 t15 0 t15 0 t15 0 t15 0 t15 0 t15 0 t15 0 t15 0 t15 0 t15 0" fill="none" stroke="#4fb8b8" stroke-width="2.5"/>
  </svg>

  <p class="headline headline--fun">FUN DASH <span class="script">and</span> PARTY</p>
  <p class="date date--sunday">SUNDAY 12 SEPTEMBER</p>
  <p class="headline headline--way">YOUR WAY <span class="script">any</span> DAY</p>
  <p class="date date--month">ALL OF SEPTEMBER</p>

  <svg class="wave wave--bottom" viewBox="0 0 240 14" preserveAspectRatio="none" aria-hidden="true">
    <path d="M0 7 q7.5 -6 15 0 t15 0 t15 0 t15 0 t15 0 t15 0 t15 0 t15 0 t15 0 t15 0 t15 0 t15 0 t15 0 t15 0 t15 0 t15 0" fill="none" stroke="#4fb8b8" stroke-width="2.5"/>
  </svg>

  <p class="register">REGISTER OR SUPPORT A PARTICIPANT AT:</p>
  <p class="website">TAMSINSDASH.COM</p>

  <svg class="footer-band" viewBox="0 0 969 170" preserveAspectRatio="none" aria-hidden="true">
    <path d="M0 40 C200 0 420 0 620 30 C780 55 880 40 969 20 L969 170 L0 170 Z" fill="#faf6ee"/>
  </svg>

  <div class="foundation-mark"><span class="dot"></span>ETH Foundation</div>

  <p class="supported">PROUDLY SUPPORTED BY</p>
  <div class="sponsors">
    <span class="sponsor">Fresh Aisle</span>
    <span class="sponsor">Nimbusly</span>
    <span class="sponsor">Signa</span>
    <span class="sponsor">Harbourline</span>
    <span class="sponsor">Kaito</span>
  </div>
</main>
</body>
</html>
```